LGBTQ design for lovers chocolate box

I already have box design, I need art work for the box, The brand name is Bright Meadow
I would like silver and Gold foil used in the top cover omage as well as the insert inside the box, see image of box Vorn is not my brand so please dont copy it, use it as getting to know the box being used.
I am open to ideas on how to attract the gay LGBTQ customers
I want to use silver foil on sides of box for
Aaphrodisiac sex Chocolate
Dark Sex Chocolate
6 Serve's of Sex Chocolte
I would like to use the logo lip inside the box, there are three stations to hold 3 (50mm square chocolates) can you maybe make the logo with three seperate theems of LGBTQ
I want the top of the box with color and fun resembling the domain name - brightmeadow.fun
The inside of the box can be gold or silver foil. Any questions please ask

I have added a few other images, dont think you have to use them, i may give you another idea

A lot of designers have said they will provide a design but they have not submitted one yet. So I want to allow them the time to add there design

```html
<!DOCTYPE html>
<html lang="en">
<head>
<meta charset="utf-8">
<title>Bright Meadow – Box Insert Variations</title>
<link rel="stylesheet" href="https://fonts.googleapis.com/css2?family=Kaushan+Script&display=swap">
<style>
  :root {
    --page: #ffffff;
    --gold-deep: #efcf00;
    --gold-mid: #f6df4a;
    --gold-light: #fff4ad;
    --black: #000000;
    --ink: #111111;
    --gold-text: #f3d23a;
    --purple: #7a3f98;
    --blue: #24409a;
    --green: #0a9b48;
    --yellow: #fde01a;
    --orange: #ee6d23;
    --red: #e42a23;
  }
  * { margin: 0; padding: 0; box-sizing: border-box; }
  html, body {
    width: 1200px;
    height: 771px;
    overflow: hidden;
    background: var(--page);
  }
  .sheet {
    position: relative;
    width: 1200px;
    height: 771px;
  }
  .insert {
    position: absolute;
    top: 77px;
    width: 226px;
    height: 591px;
    overflow: hidden;
  }
  .insert--gold, .insert--glow {
    background: linear-gradient(155deg,
      var(--gold-deep) 0%,
      var(--gold-light) 12%,
      var(--gold-deep) 24%,
      var(--gold-mid) 34%,
      var(--gold-light) 44%,
      var(--gold-deep) 56%,
      var(--gold-light) 70%,
      var(--gold-deep) 84%,
      var(--gold-mid) 100%);
  }
  .insert--gold { left: 150px; }
  .insert--black { left: 481px; background: var(--black); }
  .insert--glow { left: 813px; }

  .insert__glow {
    position: absolute;
    left: 18px;
    top: 160px;
    width: 190px;
    height: 290px;
    border-radius: 50%;
    background: radial-gradient(ellipse at center, #ffffff 55%, rgba(255,255,255,0.8) 68%, rgba(255,255,255,0) 100%);
  }
  .insert__emblem {
    position: absolute;
    width: 144px;
    height: 234px;
    border-radius: 48% / 50%;
    background: linear-gradient(180deg,
      var(--purple) 0%, var(--purple) 12%,
      var(--blue) 20%, var(--blue) 34%,
      var(--green) 40%, var(--green) 52%,
      var(--yellow) 58%, var(--yellow) 70%,
      var(--orange) 76%, var(--orange) 86%,
      var(--red) 92%, var(--red) 100%);
  }
  .insert--gold .insert__emblem { left: 47px; top: 179px; }
  .insert--black .insert__emblem { left: 47px; top: 180px; width: 143px; height: 230px; }
  .insert--glow .insert__emblem { left: 43px; top: 176px; width: 148px; height: 242px; }

  .insert__brand {
    position: absolute;
    top: 418px;
    writing-mode: vertical-rl;
    font-family: "Kaushan Script", cursive;
    font-size: 24px;
    line-height: 1;
    white-space: nowrap;
    color: var(--ink);
  }
  .insert--gold .insert__brand { left: 27px; }
  .insert--black .insert__brand { left: 27px; color: var(--gold-text); }
  .insert--glow .insert__brand { left: 27px; }
</style>
</head>
<body>
  <main class="sheet">
    <section class="insert insert--gold">
      <div class="insert__emblem" role="img" aria-label="Rainbow lip-print emblem in pride colours"></div>
      <p class="insert__brand">Bright Meadow</p>
    </section>

    <section class="insert insert--black">
      <div class="insert__emblem" role="img" aria-label="Rainbow lip-print emblem in pride colours"></div>
      <p class="insert__brand">Bright Meadow</p>
    </section>

    <section class="insert insert--glow">
      <div class="insert__glow"></div>
      <div class="insert__emblem" role="img" aria-label="Rainbow lip-print emblem in pride colours on a white halo"></div>
      <p class="insert__brand">Bright Meadow</p>
    </section>
  </main>
</body>
</html>
```